Website for a company offering full serivce charging solutions for electric cars

The company "mero-kant" (english: "mero-edge") offering all-in-one-solutions for charging infrastructure for electric mobility.

There are four products:
1- Wallboxes for single-family homes
2- Solutions for property devloper/-management for property parking space
3- All-in-one-charging solution for municipalities/communities
4- Solutions for tourism/hotels/holiday appartments

The Website structure:
1. Main Page
2.1. Product Page Single Homes
2.2. Product Page Property Management / Parking
2.3. Product Page Municipality
2.4. Product Page Tourism
3. Contact Form / Request for information
4. Imprint / Legal

The Website should be built on Wordpress with a powerful possibility to simply add/modify specific landing pages.

We would like you to implement the website later and also maintain it if possible, but we would be able to do minor modifications by ourselfs (for A/B-Testing)

The website should be clear and simple, easy to understand.
Target group is mainly B2C without deeper knowledge of that topic.

It should suggest, that we will provide a very simple way to get the charging infrastructure done.

We need a contact form, maybe we will use Hubspot later.

Attached you will find a draft of the main page and a landing page (for 2.2) - it is just the content, please ignore the design. We would love to let you create a suitable design.
Also you will find some drafts a bit different for the same story.

I added also a few stock photos, but they don't need to be used! If you have better ideas, you are welcome!

Industry/Entity Type

Charging/Electric mobility

Number of Pages Required

2 page

Font styles to use
Sans Serif

Requirements
Must have
• Based on Wordpress, and the designer should be able to implement it on Wordpress on a later step

```html
<!DOCTYPE html>
<html lang="de">
<head>
<meta charset="utf-8">
<title>mero-kant – Lösungen für Gemeinden</title>
<link href="https://fonts.googleapis.com/css2?family=Audiowide&family=Poppins:wght@400;500;600&display=swap" rel="stylesheet">
<style>
  :root {
    --ink: #141b2b;
    --text: #2b2f3a;
    --muted: #4a4e59;
    --pink: #e90f9d;
    --violet: #7a63c8;
    --navy: #0f1523;
    --white: #ffffff;
  }
  * { box-sizing: border-box; margin: 0; padding: 0; }
  html, body { width: 1200px; height: 2375px; overflow: hidden; }
  body {
    position: relative;
    background: var(--white);
    font-family: "Poppins", sans-serif;
    color: var(--text);
  }
  .heading {
    font-family: "Audiowide", sans-serif;
    font-weight: 400;
    color: var(--ink);
    font-size: 32px;
    line-height: 33px;
    letter-spacing: 2px;
  }
  p { font-size: 14px; line-height: 22px; color: var(--muted); }
  .abs { position: absolute; }

  /* header */
  .brand { display: flex; align-items: center; gap: 10px; text-decoration: none; }
  .brand-dot { width: 34px; height: 34px; border-radius: 50%; background: var(--pink); }
  .brand-name { font-family: "Poppins", sans-serif; font-weight: 500; font-size: 28px; color: var(--ink); }
  .site-header .brand { left: 89px; top: 26px; }
  .main-nav { left: 607px; top: 26px; display: flex; align-items: center; gap: 30px; }
  .main-nav a { font-size: 15px; color: var(--ink); text-decoration: none; }
  .main-nav a.is-active { color: var(--pink); }
  .btn-outline {
    display: inline-block; padding: 9px 26px; border-radius: 22px;
    border: 2px solid var(--pink); border-right-color: var(--violet);
    font-size: 12px; font-weight: 600; letter-spacing: .5px;
  }

  /* hero */
  .hero-title { left: 88px; top: 204px; width: 570px; }
  .hero-lead { left: 88px; top: 344px; width: 600px; font-size: 15px; line-height: 24px; color: var(--text); font-weight: 500; }
  .hero-copy { left: 88px; top: 402px; width: 620px; }
  .hero-copy p + p { margin-top: 7px; }
  .hero-illustration {
    left: 737px; top: 150px; width: 410px; height: 432px; border-radius: 50%;
    background: radial-gradient(circle at 55% 50%, #d13fb8 0%, #8a4fd0 35%, #eef0f2 62%, #ffffff 75%);
    border: 8px solid #1e2a31;
  }

  /* waves */
  .wave-soft { left: 0; top: 900px; width: 1200px; height: 960px; }
  .wave-footer { left: 0; top: 1835px; width: 1200px; height: 540px; }

  /* coordination */
  .photo-accent { left: 337px; top: 897px; width: 226px; height: 242px; border-radius: 6px;
    background: linear-gradient(90deg, var(--pink), var(--violet)); }
  .photo { left: 88px; top: 634px; width: 456px; height: 487px; border-radius: 20px;
    background: linear-gradient(135deg, #5f7691 0%, #b8c6d2 35%, #e9e4df 55%, #4b4f55 80%, #8e979f 100%); }
  .coord-title { left: 600px; top: 745px; width: 530px; }
  .coord-copy { left: 600px; top: 899px; width: 530px; }
  .coord-copy p + p { margin-top: 7px; }

  /* columns */
  .col { top: 1420px; width: 500px; }
  .col-left { left: 88px; }
  .col-right { left: 621px; }
  .col .heading { margin-bottom: 8px; }
  .col p + p { margin-top: 11px; }
  .btn-primary {
    display: inline-block; margin-top: 26px; padding: 17px 34px; border-radius: 27px;
    background: linear-gradient(90deg, var(--pink), var(--violet));
    color: var(--white); font-size: 13px; font-weight: 600; letter-spacing: .5px; text-decoration: none;
  }

  /* footer */
  .site-footer .brand { left: 0; width: 1200px; top: 2115px; justify-content: center; }
  .site-footer .brand-name { color: var(--white); font-size: 31px; }
  .footer-nav { left: 0; width: 1200px; top: 2181px; display: flex; justify-content: center; gap: 22px; }
  .footer-nav a { color: var(--white); text-decoration: none; font-size: 15.5px; }
  .social { left: 0; width: 1200px; top: 2228px; display: flex; justify-content: center; gap: 8px; }
  .social span { width: 43px; height: 43px; border-radius: 50%; background: #1d2434; }
  .footer-rule { left: 88px; top: 2329px; width: 1022px; height: 1px; background: #2b3242; }
  .copyright { left: 0; width: 1200px; top: 2342px; text-align: center; font-size: 14px; color: var(--white); }
  .to-top { left: 1130px; top: 2305px; width: 34px; height: 34px; border-radius: 50%;
    background: linear-gradient(135deg, var(--pink), var(--violet)); display: flex; align-items: center; justify-content: center; }
</style>
</head>
<body>
  <svg class="abs wave-soft" viewBox="0 0 1200 960" preserveAspectRatio="none" aria-hidden="true">
    <defs>
      <linearGradient id="softFill" x1="0" y1="0" x2="1" y2="0">
        <stop offset="0" stop-color="#fbe0f1"/>
        <stop offset="1" stop-color="#efe9f8"/>
      </linearGradient>
      <linearGradient id="fadeOut" x1="0" y1="0" x2="0" y2="1">
        <stop offset="0" stop-color="#fff" stop-opacity="0"/>
        <stop offset="0.55" stop-color="#fff" stop-opacity="0"/>
        <stop offset="1" stop-color="#fff" stop-opacity="1"/>
      </linearGradient>
    </defs>
    <path d="M0 12 C120 -10 220 20 300 130 C380 250 430 372 500 372 C620 372 700 320 790 270 C880 220 960 210 1040 235 C1110 260 1160 290 1200 320 L1200 960 L0 960 Z" fill="url(#softFill)"/>
    <rect x="0" y="0" width="1200" height="960" fill="url(#fadeOut)"/>
  </svg>

  <header class="site-header">
    <a class="abs brand" href="#"><span class="brand-dot"></span><span class="brand-name">mero-kant.de</span></a>
    <nav class="abs main-nav">
      <a class="is-active" href="#">Lösungen</a>
      <a href="#">Unternehmen</a>
      <a href="#">Services</a>
      <a href="#">Karriere</a>
      <a class="btn-outline" href="#">KONTAKT</a>
    </nav>
  </header>

  <section class="hero">
    <h1 class="abs heading hero-title">Wir bringen Ihre Gemeinde mit klimafördernden Maßnahmen in die Schlagzeilen</h1>
    <p class="abs hero-lead">Ohne entsprechende Lade-Infrastruktur für E-Autos für Bürger aber auch Besucher der Gemeinde wird E-Mobilität nicht den notwendigen Drive erfahren.</p>
    <div class="abs hero-copy">
      <p>kümmern uns darum, dass Ihre Ladesäulen gefunden werden, und tragen Sie in den gängigen Ladenetzportalen ein.</p>
      <p>Nicht jeder Bürger hat die Möglichkeit sich eine Lademöglichkeit zu Hause aufzubauen. Besucher aus der Umgebung sind dankbar und suchen nach Lademöglichkeiten an ihrem Ausflugsziel, aufgrund mangelnder Lademöglichkeiten in der Stadt.</p>
    </div>
    <div class="abs hero-illustration" role="img" aria-label="Illustration: Elektroauto in einem Kreis mit Öltropfen, Zapfpistole, Stecker und Blitzsymbol"></div>
  </section>

  <section class="coordination">
    <div class="abs photo-accent"></div>
    <div class="abs photo" role="img" aria-label="Foto: Hand hält einen Ladestecker vor einem Elektroauto"></div>
    <h2 class="abs heading coord-title">Wir übernehmen die Koordination und Finanzierung und lassen Sie dennoch mit verdienen</h2>
    <div class="abs coord-copy">
      <p>Unser Angebot ist es Ihnen der Gemeinde die notwendige Infrastruktur zu finanzieren, den Aufbau zu organisieren, und den 24/7 Betrieb sicherzustellen.</p>
      <p>Neben der Unterstützung der lokalen Infrastruktur sollen sie als Gemeinde auch an den Erlösen der Ladevorgänge beteiligt sein.</p>
    </div>
  </section>

  <section class="benefits">
    <div class="abs col col-left">
      <h2 class="heading">Wir rechnen mit dem Kunden direkt ab</h2>
      <p>Gleichgültig wie der Kunde seinen Ladevorgang bezahlen möchte, wir bieten ihm die einfachste Lösung.</p>
      <p>Angeschlossen an die üblichen Roamingpartner kann der Kunde mit seiner bestehenden Ladekarte (AVKR, Netzwelle, ladekreis, etc.) zahlen, oder aber auch direkt per Kreditkarte, ZahlPunkt oder weiteren Zahlungsmöglichkeiten</p>
      <p>Wir rechnen den Kunden exakt nach seinem bezogenen Stromverbrauch ab. Keine unfaire Pauschal- oder Standzeitabrechnung. Wir werden frühestens nach 3.5 Stunden eine Branchen übliche Belegungsgebühr erheben, sollte der Ladevorgang bereits abgeschlossen sein.</p>
    </div>
    <div class="abs col col-right">
      <h2 class="heading">Wir verstehen die Kommunen als unsere Partner</h2>
      <p>Trotzdem, dass wir die Kosten für Infrastruktur und Installation übernehmen, den Betrieb sicherstellen, und den Kunden ein einwandfreies Laderlebnis garantieren, beteiligen wir Sie als unseren Partner am Erfolg.</p>
      <p>Neben der anteiligen Umsatzbeteiligung bieten wir die Möglichkeit der Integration des lokaler Einzelhandels über ein Bonusprogramm. Ebenso besteht die Möglichkeit ihre bereits vorhandene Parkraumüberwachung in unser Konzept zu integrieren.</p>
      <a class="btn-primary" href="#">SPRECHEN SIE JETZT MIT UNS</a>
    </div>
  </section>

  <footer class="site-footer">
    <svg class="abs wave-footer" viewBox="0 0 1200 540" preserveAspectRatio="none" aria-hidden="true">
      <defs>
        <linearGradient id="bandFill" x1="0" y1="0" x2="1" y2="0">
          <stop offset="0" stop-color="#e90f9d"/>
          <stop offset="0.6" stop-color="#9b46c4"/>
          <stop offset="1" stop-color="#7a63c8"/>
        </linearGradient>
      </defs>
      <path d="M0 190 C120 120 220 0 330 10 C470 20 560 120 700 190 C820 250 960 260 1060 200 C1130 160 1175 110 1200 60 L1200 540 L0 540 Z" fill="url(#bandFill)"/>
      <path d="M0 240 C110 170 230 50 340 50 C480 50 580 150 720 220 C840 275 970 265 1070 210 C1135 172 1178 125 1200 90 L1200 540 L0 540 Z" fill="#0f1523"/>
    </svg>
    <a class="abs brand" href="#"><span class="brand-dot"></span><span class="brand-name">mero-kant.de</span></a>
    <nav class="abs footer-nav">
      <a href="#">AGB</a><a href="#">Datenschutzerklärung</a><a href="#">Impressum</a><a href="#">Kontakt</a><a href="#">Karriere</a><a href="#">FAQs</a>
    </nav>
    <div class="abs social">
      <span role="img" aria-label="Soziales Netzwerk 1"></span>
      <span role="img" aria-label="Videoplattform"></span>
      <span role="img" aria-label="Soziales Netzwerk 2"></span>
    </div>
    <div class="abs footer-rule"></div>
    <p class="abs copyright">©mero-kant GmbH</p>
    <a class="abs to-top" href="#" aria-label="Nach oben">
      <svg width="12" height="12" viewBox="0 0 12 12"><path d="M3 7.5 L6 4.5 L9 7.5" fill="none" stroke="#fff" stroke-width="1.6" stroke-linecap="round"/></svg>
    </a>
  </footer>
</body>
</html>
```